Wine Label Design

We are looking for a new label to add to our winery. This is to be named "Lindgrube" which is the German word for schoolhouse. Our tasting room is a one room school house built in 1887. I would like the label to be very simple and clean with a schoolhouse on the front. I would like to schoolhouse to be sketch style, not a cartoonish design. I have attached a photo of the schoolhouse that we pour from, this is what I would want the schoolhouse to resemble. I have also added a copy of our current "higher end" label so that you have an idea of our style. I would like the new label to be cohesive with our old label and look good next to each other on our shelves. Just as added clarification we do not want Harlen Vineyards on the new label - we want that replaced with Lindgrube. If you are unable to do a full label design we would also accept just the schoolhouse drawing design as well. Thank you.

Logo Text

Lindgrube

```html
<!DOCTYPE html>
<html lang="en">
<head>
<meta charset="utf-8">
<title>Lindgrube – Dry Rosé Label</title>
<link href="https://fonts.googleapis.com/css2?family=Cinzel:wght@400;600&family=Great+Vibes&display=swap" rel="stylesheet">
<style>
  :root {
    --backdrop: #f2f2f2;
    --sheet: #ffffff;
    --label-brown: #261e14;
    --label-text: #ffffff;
    --accent-yellow: #f9e264;
    --mark-black: #000000;
  }
  html, body {
    margin: 0;
    padding: 0;
    width: 1200px;
    height: 1000px;
    overflow: hidden;
    background: var(--backdrop);
  }
  .canvas {
    position: relative;
    width: 1200px;
    height: 1000px;
  }
  .sheet {
    position: absolute;
    left: 100px;
    top: 88px;
    width: 1000px;
    height: 834px;
    background: var(--sheet);
  }
  .label {
    position: absolute;
    left: 206px;
    top: 264px;
    width: 397px;
    height: 464px;
  }
  .label-shape {
    position: absolute;
    inset: 0;
  }
  .label-content {
    position: absolute;
    inset: 0;
    color: var(--label-text);
    text-align: center;
  }
  .label-mark {
    position: absolute;
    top: 44px;
    left: 0;
    right: 0;
    font-family: "Cinzel", serif;
    font-weight: 400;
    font-size: 18px;
    letter-spacing: 2px;
    color: var(--accent-yellow);
  }
  .label-name {
    position: absolute;
    top: 120px;
    left: 0;
    right: 0;
    font-family: "Cinzel", serif;
    font-weight: 600;
    font-size: 44px;
    letter-spacing: 1.5px;
    line-height: 1;
  }
  .label-vintage {
    position: absolute;
    top: 256px;
    left: 0;
    right: 0;
    font-family: "Cinzel", serif;
    font-size: 14px;
    letter-spacing: 4px;
  }
  .label-varietal {
    position: absolute;
    top: 304px;
    left: 0;
    right: 0;
    font-family: "Great Vibes", cursive;
    font-size: 40px;
    line-height: 1;
  }
  .label-region {
    position: absolute;
    top: 398px;
    left: 0;
    right: 0;
    font-family: "Cinzel", serif;
    font-size: 14px;
    letter-spacing: 1px;
  }
  .brand-mark {
    position: absolute;
    left: 740px;
    width: 300px;
    text-align: center;
    font-family: "Cinzel", serif;
    font-weight: 400;
    font-size: 48px;
    letter-spacing: 2px;
  }
  .brand-mark--yellow {
    top: 300px;
    color: var(--accent-yellow);
  }
  .brand-mark--black {
    top: 670px;
    color: var(--mark-black);
  }
</style>
</head>
<body>
<div class="canvas">
  <div class="sheet"></div>

  <div class="label">
    <svg class="label-shape" width="397" height="464" viewBox="0 0 397 464" aria-hidden="true">
      <path d="M0 39 Q198.5 -26 397 39 L397 464 L0 464 Z" fill="var(--label-brown)"/>
    </svg>
    <div class="label-content">
      <div class="label-mark">Lindgrube</div>
      <div class="label-name">LINDGRUBE</div>
      <div class="label-vintage">2016</div>
      <div class="label-varietal">Dry Rose</div>
      <div class="label-region">Finger Lakes</div>
    </div>
  </div>

  <div class="brand-mark brand-mark--yellow">Lindgrube</div>
  <div class="brand-mark brand-mark--black">Lindgrube</div>
</div>
</body>
</html>
```